Plakat-Design für Vogelvolieren
Zielgruppe
Es geht um vier Din A4-Plakate, die an vier Vogelvolieren hängen und Informationen zu den Vögeln bieten, die sich in den Volieren befinden.
Die Volieren gehören zum Tierpark Haselbrück. Einem kleinen Wildpark, bei dem ausschließlich Ehrenamtliche tätig sind. Der Eintritt ist frei.
Die Zielgruppe sind die Besucher - von klein bis groß, von jung bis alt
Aufgabenstellung
Gute Lesbarkeit, denn die Informationsvermittlung soll im Vordergrund stehen.
Wir benötigen 1 Plakatdesign und die offenen Daten in InDesign, denn dann würden wir bei den weiteren drei Plakaten die Texte und Fotos austauschen.
Es sind 2 Plakate mit 4 Vögeln und 2 Plakate mit 2 Vögeln.

```html
<!DOCTYPE html>
<html lang="de">
<head>
<meta charset="utf-8">
<title>Vogelvolieren – Tierpark Haselbrück</title>
<link href="https://fonts.googleapis.com/css2?family=Alegreya:wght@700&family=Asap+Condensed:wght@500;600&display=swap" rel="stylesheet">
<style>
  :root{
    --bg:#dcdcdc;
    --peach:#f2d5c8;
    --green:#67a063;
    --purple:#8a2467;
    --line:#d29a4c;
    --card:#fbfbfa;
    --ink:#1f1a17;
    --white:#ffffff;
  }
  *{box-sizing:border-box;margin:0;padding:0}
  html,body{width:1200px;height:1200px;overflow:hidden;background:var(--bg)}
  .poster{
    position:absolute;left:196px;top:30px;width:808px;height:1140px;
    background:var(--peach);overflow:hidden;
    font-family:"Asap Condensed",Arial Narrow,sans-serif;color:var(--ink);
  }
  .greenery{position:absolute;inset:0;width:808px;height:1140px}
  .photo{position:absolute;border-radius:50%;box-shadow:0 0 0 9px var(--green)}
  .photo--lovebirds{left:-10px;top:-40px;width:380px;height:360px;
    background:radial-gradient(circle at 45% 45%,#b9936a,#a4774d 60%,#8a6240)}
  .photo--finch{left:434px;top:-44px;width:378px;height:378px;
    background:radial-gradient(circle at 50% 50%,#d9b985,#c9a26a 60%,#a98552)}
  .photo--quail{left:-15px;top:780px;width:410px;height:410px;
    background:linear-gradient(180deg,#b38e62 0%,#8f8276 40%,#a88f73 70%,#c3a887 100%)}
  .photo--cockatiel{left:424px;top:797px;width:400px;height:400px;
    background:radial-gradient(circle at 55% 55%,#9c9587,#7e6b57 60%,#5f5243)}
  .title{
    position:absolute;background:var(--purple);color:var(--white);
    font-family:"Alegreya",Georgia,serif;font-weight:700;
    font-size:22px;line-height:26px;text-align:center;
    display:flex;align-items:center;justify-content:center;
    border-radius:42% 48% 40% 52% / 55% 45% 55% 45%;
  }
  .title--lovebirds{left:217px;top:25px;width:192px;height:48px}
  .title--finch{left:417px;top:211px;width:154px;height:82px}
  .title--quail{left:12px;top:816px;width:172px;height:91px}
  .title--cockatiel{left:379px;top:1069px;width:201px;height:69px}
  .brand{
    position:absolute;right:0;top:0;width:150px;height:76px;background:var(--white);
    border-bottom-left-radius:90px 70px;
    display:flex;align-items:center;justify-content:flex-end;gap:5px;padding:0 10px 14px 0;
    color:var(--purple);font-weight:600;font-size:10px;line-height:12px;
  }
  .brand__dot{width:9px;height:9px;border-radius:50%;background:var(--purple)}
  .card{
    position:absolute;background:var(--card);border:1.3px solid var(--line);border-radius:22px;
    display:grid;grid-template-columns:1fr 104px;column-gap:8px;padding:14px 12px 10px 12px;
  }
  .card--lovebirds{left:16px;top:313px;width:372px;height:244px}
  .card--finch{left:406px;top:312px;width:384px;height:252px}
  .card--quail{left:21px;top:567px;width:384px;height:257px}
  .card--cockatiel{left:423px;top:574px;width:373px;height:274px}
  .card h3{color:var(--purple);font-weight:600;font-size:15px;text-decoration:underline;text-underline-offset:2px;text-align:center;margin-bottom:8px}
  .card p{font-size:11.3px;line-height:16.5px;text-align:center}
  .card p+p{margin-top:6px}
  .card__wide{grid-column:1 / -1;margin-top:4px}
  .map{width:100px;height:48px;margin:0 auto 12px;border-radius:8px;
    background:linear-gradient(90deg,var(--green),#7fae74 50%,var(--green))}
  .pointer{position:absolute;width:28px;height:30px;overflow:visible}
</style>
</head>
<body>
<main class="poster">
  <svg class="greenery" viewBox="0 0 808 1140" aria-hidden="true">
    <path fill="#67a063" d="M0 0H808V285C760 300 720 290 690 300C620 318 560 292 500 300C450 306 420 290 380 284C330 276 300 298 250 296C200 294 140 302 90 296C50 292 20 300 0 298Z"/>
    <path fill="#67a063" d="M0 1040C40 1010 70 990 120 985C200 980 260 960 330 948C380 940 420 960 460 950C520 935 560 955 620 948C700 940 760 960 808 935V1140H0Z"/>
  </svg>

  <div class="photo photo--lovebirds" role="img" aria-label="Foto: zwei Unzertrennliche, grün mit rotem Kopf und türkis, auf einem Ast"></div>
  <div class="photo photo--finch" role="img" aria-label="Foto: Zebrafink mit rotem Schnabel auf einer Stange"></div>
  <div class="photo photo--quail" role="img" aria-label="Foto: Europäische Wachtel auf Körnerstreu"></div>
  <div class="photo photo--cockatiel" role="img" aria-label="Foto: Sittich mit gelber Haube auf einem Holzrand in der Voliere"></div>

  <div class="brand"><span class="brand__dot"></span><span>Tierpark<br>Haselbrück</span></div>

  <h2 class="title title--lovebirds">Unzertrennliche</h2>
  <h2 class="title title--finch">Australische<br>Zebrafinken</h2>
  <h2 class="title title--quail">Europäische<br>Wachteln</h2>
  <h2 class="title title--cockatiel">Katharinasittiche</h2>

  <section class="card card--lovebirds">
    <div>
      <h3>Aussehen:</h3>
      <p>Ihre Farbgebung gibt den verschiedenen Arten ihren Namen. Es gibt Grauköpfchen, Orangeköpfchen, Tarantapapageien, Grünköpfchen, Rosenköpfchen, Pfirsichköpfchen, Schwarzköpfchen, Erdbeerköpfchen und Rußköpfchen.</p>
      <p>Unzertrennliche werden rund 13 bis 18 Zentimeter lang und wiegen etwa 50 Gramm.</p>
    </div>
    <div>
      <h3>Vorkommen:</h3>
      <div class="map" role="img" aria-label="Weltkarte mit markiertem Afrika"></div>
      <p>Unzertrennliche leben in Afrika sowohl in heißen Savannen als auch in feucht-tropischen Regenwäldern.</p>
    </div>
  </section>

  <section class="card card--finch">
    <div>
      <h3>Aussehen:</h3>
      <p>Gut zu erkennen sind Zebrafinken an ihrem orange-roten Schnabel, am schwarzen Tränenstrich unter den Augen und der schwarzen Zebra-Musterung der Brust. Das Gefieder der Männchen, die über einen orange-farbenen Wangenfleck verfügen, ist kräftiger als das der Weibchen. Ihre kurzen, eckigen Flügel machen Zebrafinken zu wahren Flugakrobaten.</p>
    </div>
    <div>
      <h3>Vorkommen:</h3>
      <div class="map" role="img" aria-label="Weltkarte mit markiertem Australien"></div>
      <p>Australische Zebrafinken leben fast überall in Australien.</p>
    </div>
    <p class="card__wide">Zebrafinken werden rund 12 Zentimeter lang<br>und wiegen 12 bis 14 Gramm.</p>
  </section>

  <section class="card card--quail">
    <div>
      <h3>Aussehen:</h3>
      <p>Europäische Wachteln, die auch als Feldwachteln bezeichnet werden, haben eine graubraune Gesamtfärbung mit einer Vielzahl rotbrauner und schwarzer Striche. Die Flügel sind grau. Die Augenfarbe ist rotbraun und damit ein Unterscheidungsmerkmal, denn die japanischen Zuchtwachteln haben dunkle Augen.</p>
      <p>Wachteln wiegen rund<br>90 bis 100 Gramm.</p>
    </div>
    <div>
      <h3>Vorkommen:</h3>
      <div class="map" role="img" aria-label="Weltkarte mit markiertem Europa, Westasien und Afrika"></div>
      <p>Europäische Wachteln leben in fast ganz Europa, den westlichen Teil Asiens und einem großen Teil Afrikas.</p>
    </div>
  </section>

  <section class="card card--cockatiel">
    <div>
      <h3>Aussehen:</h3>
      <p>Mit ihrem leuchtend grünen Gefieder mit blauschwarzen Abzeichen sind Katharinasittiche perfekt an die Wälder in ihrer Heimat angepasst. Aufgrund von gezielten Züchtungen gibt es mittlerweile auch gelbe, blaue, türkis- und creme-farbene Katharinasittiche. Männliche und weibliche Katharinasittiche lassen sich äußerlich kaum unterscheiden.</p>
    </div>
    <div>
      <h3>Vorkommen:</h3>
      <div class="map" role="img" aria-label="Weltkarte mit markiertem Mittel- und Südamerika"></div>
      <p>Katharinasittiche leben in Mittel- und Südamerika.</p>
    </div>
    <p class="card__wide">Erwachsene Vögel werden 16 bis 17 Zentimeter lang, wobei der Schwanz rund 6 Zentimeter misst, und wiegen etwa 50 bis 60 Gramm.</p>
  </section>

  <svg class="pointer" style="left:262px;top:285px" viewBox="0 0 28 30" aria-hidden="true"><path d="M0 30 L2 0 L26 30" fill="#fbfbfa" stroke="#d29a4c" stroke-width="1.3"/></svg>
  <svg class="pointer" style="left:566px;top:284px" viewBox="0 0 28 30" aria-hidden="true"><path d="M2 30 L26 0 L24 30" fill="#fbfbfa" stroke="#d29a4c" stroke-width="1.3"/></svg>
  <svg class="pointer" style="left:268px;top:822px" viewBox="0 0 28 30" aria-hidden="true"><path d="M2 0 L2 30 L28 0" fill="#fbfbfa" stroke="#d29a4c" stroke-width="1.3"/></svg>
  <svg class="pointer" style="left:482px;top:846px" viewBox="0 0 28 30" aria-hidden="true"><path d="M0 0 L26 30 L26 0" fill="#fbfbfa" stroke="#d29a4c" stroke-width="1.3"/></svg>
</main>
</body>
</html>
```